Tallowreed Advisory Partners Business Card Design

We have the logo we just need someone to design a modern business card design.

Name: Desmond Munkalt
Phone: 3055550148
Mobile: 9175550193
Web:www.tallowreedadvisory.example
email: dmunkalt@tallowreedadvisory.example
Company: Tallowreed Advisory Partners
Title: CEO

Address: 718 Quillmore Ave, Miami, Florida 33190

Target Market(s)

companies over 100 employees

Industry/Entity Type

Business

```html
<!DOCTYPE html>
<html lang="en">
<head>
<meta charset="utf-8">
<title>Tallowreed Advisory Partners — Business Card</title>
<link href="https://fonts.googleapis.com/css2?family=Open+Sans:wght@400;600;700&display=swap" rel="stylesheet">
<style>
  :root {
    --page: #e6e6e6;
    --card-dark: #161616;
    --card-light: #f7f7f7;
    --brand-blue: #3445a8;
    --ink: #2a2a2a;
    --muted: #6b6b6b;
    --white: #ffffff;
  }
  * { box-sizing: border-box; margin: 0; padding: 0; }
  html, body { width: 1200px; height: 1200px; overflow: hidden; }
  body {
    background: var(--page);
    font-family: "Open Sans", Arial, sans-serif;
    position: relative;
  }
  .card {
    position: absolute;
    left: 250px;
    width: 700px;
    height: 400px;
    border-radius: 6px;
    overflow: hidden;
    box-shadow: 0 10px 30px rgba(0,0,0,0.15);
  }
  /* Front */
  .card-front { top: 140px; background: var(--card-dark); }
  .front-texture {
    position: absolute; inset: 0;
    background:
      radial-gradient(ellipse 70% 45% at 60% 25%, rgba(200,200,200,0.45), transparent 70%),
      radial-gradient(ellipse 50% 30% at 80% 45%, rgba(160,160,160,0.3), transparent 70%),
      linear-gradient(160deg, #2a2a2a 0%, #141414 60%, #0e0e0e 100%);
  }
  .front-brand {
    position: absolute; left: 0; right: 0; top: 150px;
    display: flex; flex-direction: column; align-items: center; gap: 14px;
  }
  .brand-dot {
    width: 78px; height: 78px; border-radius: 50%;
    background: var(--brand-blue);
  }
  .brand-name {
    font-weight: 700; text-transform: uppercase; text-align: center;
    letter-spacing: 2px; line-height: 1.15;
  }
  .front-brand .brand-name { color: var(--white); font-size: 34px; }
  .front-brand .brand-name span { display: block; font-size: 13px; letter-spacing: 3px; }

  /* Back */
  .card-back { top: 640px; background: var(--card-light); }
  .back-brand {
    position: absolute; right: 40px; top: 38px;
    display: flex; flex-direction: column; align-items: center; gap: 8px;
  }
  .back-brand .brand-dot { width: 58px; height: 58px; }
  .back-brand .brand-name { color: var(--ink); font-size: 24px; }
  .back-brand .brand-name span { display: block; font-size: 9px; letter-spacing: 2px; }
  .name-band {
    position: absolute; left: 0; right: 0; top: 180px; height: 46px;
    background: var(--brand-blue);
    display: flex; align-items: center; padding-left: 40px; gap: 14px;
    color: var(--white);
  }
  .person-name { font-weight: 700; font-size: 21px; }
  .person-title {
    font-size: 14px; padding-left: 14px;
    border-left: 1px solid rgba(255,255,255,0.7);
  }
  .contact-list {
    position: absolute; left: 40px; top: 250px;
    list-style: none; display: flex; flex-direction: column; gap: 8px;
    color: var(--ink); font-size: 15px;
  }
  .contact-list li, .phone-list li { display: flex; align-items: center; gap: 10px; }
  .icon {
    width: 20px; height: 20px; border-radius: 50%;
    background: var(--ink); flex: none;
    display: flex; align-items: center; justify-content: center;
  }
  .icon svg { width: 12px; height: 12px; }
  .divider {
    position: absolute; left: 450px; top: 250px; width: 1px; height: 80px;
    background: #b5b5b5;
  }
  .phone-list {
    position: absolute; left: 475px; top: 255px;
    list-style: none; display: flex; flex-direction: column; gap: 10px;
    color: var(--ink); font-size: 18px; letter-spacing: 0.5px;
  }
</style>
</head>
<body>

  <section class="card card-front">
    <div class="front-texture" role="img" aria-label="Dark background with a soft silver dotted wave texture"></div>
    <div class="front-brand">
      <div class="brand-dot"></div>
      <div class="brand-name">Tallowreed<span>Advisory Partners</span></div>
    </div>
  </section>

  <section class="card card-back">
    <div class="back-brand">
      <div class="brand-dot"></div>
      <div class="brand-name">Tallowreed<span>Advisory Partners</span></div>
    </div>

    <div class="name-band">
      <span class="person-name">Desmond Munkalt</span>
      <span class="person-title">CEO</span>
    </div>

    <ul class="contact-list">
      <li>
        <span class="icon"><svg viewBox="0 0 12 12"><path d="M6 1a3.5 3.5 0 0 0-3.5 3.5C2.5 7 6 11 6 11s3.5-4 3.5-6.5A3.5 3.5 0 0 0 6 1zm0 5a1.4 1.4 0 1 1 0-2.8A1.4 1.4 0 0 1 6 6z" fill="#fff"/></svg></span>
        718 Quillmore Ave, Miami, Florida 33190
      </li>
      <li>
        <span class="icon"><svg viewBox="0 0 12 12"><rect x="1.5" y="3" width="9" height="6" fill="none" stroke="#fff"/><path d="M1.5 3 6 6.5 10.5 3" fill="none" stroke="#fff"/></svg></span>
        dmunkalt@tallowreedadvisory.example
      </li>
      <li>
        <span class="icon"><svg viewBox="0 0 12 12"><circle cx="6" cy="6" r="4.5" fill="none" stroke="#fff"/><ellipse cx="6" cy="6" rx="2" ry="4.5" fill="none" stroke="#fff"/><path d="M1.5 6h9" stroke="#fff"/></svg></span>
        www.tallowreedadvisory.example
      </li>
    </ul>

    <div class="divider"></div>

    <ul class="phone-list">
      <li>
        <span class="icon"><svg viewBox="0 0 12 12"><path d="M3 1.5h2l.8 2.3-1.2.9a6 6 0 0 0 2.7 2.7l.9-1.2 2.3.8v2A1 1 0 0 1 9.5 10 8 8 0 0 1 2 2.5a1 1 0 0 1 1-1z" fill="#fff"/></svg></span>
        3055550148
      </li>
      <li>
        <span class="icon"><svg viewBox="0 0 12 12"><rect x="3.5" y="1" width="5" height="10" rx="1" fill="none" stroke="#fff"/><circle cx="6" cy="9.3" r="0.6" fill="#fff"/></svg></span>
        9175550193
      </li>
    </ul>
  </section>

</body>
</html>
```